Redesign Colorful Business Card

Please redesign the card attached. It is too busy. Please don't eliminate any of the words. The repetivite word "free" can be used less often.

Target Market(s)

College Students.

Contact Information for Business Card

The details listed in the attached image

Font styles to use
Sans Serif

Requirements
Must have
• A clear and simple presentation and must be attractive.

```html
<!DOCTYPE html>
<html lang="en">
<head>
<meta charset="utf-8">
<title>StudyBrisk.com Business Card</title>
<link rel="stylesheet" href="https://fonts.googleapis.com/css2?family=Poppins:wght@400;500;600&display=swap">
<style>
  :root {
    --page-bg: #e9e4dc;
    --red: #e8262b;
    --orange: #e4892e;
    --purple: #b04fa0;
    --sky: #8fb7d6;
    --teal: #6cc7d6;
    --white: #ffffff;
    --mascot-a: #a0607f;
    --mascot-b: #8a5a86;
    --badge-yellow: #ffe500;
    --badge-ink: #1d1d1d;
  }
  * { margin: 0; padding: 0; box-sizing: border-box; }
  html, body {
    width: 900px; height: 1200px; overflow: hidden;
    background: var(--page-bg);
    font-family: "Poppins", sans-serif;
  }
  .canvas { position: relative; width: 900px; height: 1200px; }

  .card {
    position: absolute; left: 82px; width: 733px; height: 430px;
    border-radius: 22px; overflow: hidden;
    box-shadow: 0 6px 14px rgba(0,0,0,0.3);
  }
  .card-front {
    top: 137px;
    background:
      radial-gradient(circle at 0% 35%, var(--sky) 0%, rgba(143,183,214,0) 35%),
      radial-gradient(circle at 100% 0%, var(--teal) 0%, rgba(108,199,214,0) 22%),
      radial-gradient(circle at 100% 55%, var(--purple) 0%, rgba(176,79,160,0) 45%),
      radial-gradient(circle at 60% 100%, var(--orange) 0%, rgba(228,137,46,0) 40%),
      radial-gradient(circle at 100% 100%, var(--teal) 0%, rgba(108,199,214,0) 12%),
      var(--red);
  }
  .card-back {
    top: 632px;
    background:
      radial-gradient(circle at 0% 0%, #dfe9f2 0%, rgba(143,183,214,0.9) 18%, rgba(143,183,214,0) 40%),
      radial-gradient(circle at 100% 0%, var(--orange) 0%, rgba(228,137,46,0) 40%),
      radial-gradient(circle at 100% 100%, var(--purple) 0%, rgba(176,79,160,0) 45%),
      radial-gradient(circle at 60% 55%, #e8502a 0%, rgba(232,80,42,0) 30%),
      var(--red);
  }

  .ring { position: absolute; inset: 0; }

  .mascot-area {
    position: absolute; border-radius: 30px;
    background: linear-gradient(160deg, var(--mascot-a), var(--mascot-b));
    opacity: 0.85;
  }
  .card-front .mascot-area { left: 258px; top: 33px; width: 272px; height: 280px; }
  .card-back .mascot-area {
    left: 0; top: 18px; width: 296px; height: 412px; border-radius: 0 30px 0 0;
  }

  .brand-name {
    position: absolute; left: 0; right: 0; top: 330px;
    text-align: center; color: var(--white);
    font-weight: 500; font-size: 44px; line-height: 1;
  }
  .copyright {
    position: absolute; left: 0; right: 0; top: 382px;
    text-align: center; color: var(--white);
    font-weight: 500; font-size: 16px; letter-spacing: 1.1px;
  }

  .benefits { position: absolute; left: 328px; top: 80px; list-style: none; }
  .benefit { display: flex; align-items: flex-start; height: 105px; }
  .free-badge {
    flex: none; width: 58px; height: 34px; margin-top: 12px; margin-right: 22px;
    background: var(--badge-yellow); color: var(--badge-ink);
    border-radius: 4px; transform: rotate(-4deg);
    font-weight: 600; font-size: 15px; line-height: 34px; text-align: center;
    box-shadow: 2px 2px 0 rgba(0,0,0,0.25);
  }
  .benefit-text {
    color: var(--white); font-weight: 400; font-size: 22px; line-height: 30px;
  }
</style>
</head>
<body>
<main class="canvas">
  <section class="card card-front">
    <svg class="ring" width="733" height="430" viewBox="0 0 733 430" aria-hidden="true">
      <circle cx="375" cy="-180" r="440" fill="#ef4a4c" opacity="0.55"/>
      <circle cx="375" cy="-180" r="440" fill="none" stroke="#ffffff" stroke-width="32"/>
    </svg>
    <div class="mascot-area" role="img" aria-label="Colourful elephant mascot"></div>
    <h1 class="brand-name">StudyBrisk.com</h1>
    <p class="copyright">COPYRIGHT BRISK SERVICES, LLC 2013-2022 ALL RIGHTS RESERVED</p>
  </section>

  <section class="card card-back">
    <div class="mascot-area" role="img" aria-label="Close-up of the colourful elephant mascot"></div>
    <ul class="benefits">
      <li class="benefit"><span class="free-badge">FREE</span><span class="benefit-text">CUT STUDY TIME<br>DOWN BY UP TO 50%</span></li>
      <li class="benefit"><span class="free-badge">FREE</span><span class="benefit-text">LEARN A SUBJECT WITHOUT<br>HAVING TO GO TO CLASS</span></li>
      <li class="benefit"><span class="free-badge">FREE</span><span class="benefit-text">MEMORIZE ANYTHING<br>QUICKLY</span></li>
    </ul>
  </section>
</main>
</body>
</html>
```